A new website for Electrical Contractor Business

We are looking for a unique and new WordPress website design which would include 5 Pages - Home Page, Meet the Team, Our Services, Our Projects and Contact Us page.

The global theme for the website needs to be professional but simple to navigate as we cater for both business and home owner customers.

Our core business service is targeted around lighting from single room decorative to large office so the theme should incorporate this in some way.

The home page should include;
Our business logo, Contact number, Email address, small Image rotation box - Highlighting pervious projectsText box - With welcome message, chirpnet feed news reel/Customer feed back box.

I would also like to see a 2 boxes for the separate customer types we services. Business and Home Owner. each box will have a small image with a small text description with a link to the area of the services page relevant to that customer type.

Meet the team page -This will be introducing potential customers to the team so I would like it to include for each team member. Something like a small image and text area which will introduce an outline of the team members skills and abilities.

Our Services page This page will be outlining the different services on offer to the both customer types business and homeowner. Each service should have an image with text description of the service would good here.

Our projects page-Will include images of pervious projects and work we have completed along with a text area for the project description/ outliner.

Contact Us page - Should include a contact form which should include an option for the customer to quest us to call them back, also a selection box for them to inform us our how they found our details would be good.

Colour - The theme colours can be taken from the logo or feel free to impress with your own imagination.

Remember we are looking for a website that will interest our customers enough to except our services or be drawn further into the website.. So call to action links to other areas of the site/ contact page are welcome

Target Market(s)

Business - Office, warehousing and Large Store - lighting and Power
Home owner lighting and power

Coding

Coded - Design and coding required

Number of Pages Required

5+ page

Font styles to use
Serif
Sans Serif

Colors

Designer to choose colors to be used in the design.

Requirements
Must have
• Logo integrated into the website design - i.e. website colours which allow the logo to blend into the design.
Nice to have
• Custom but professional theme catering to business customers, but also show that we do provide services to home owners too.
Should not have
• Sorry am not interested in one oversized block image on rotation covering half the home page.. Images will be needed but not a single block over sized frame with not text, shape. Please use your imagination when considering this design

```html
<!DOCTYPE html>
<html lang="en">
<head>
<meta charset="utf-8">
<title>Voltline Electrical</title>
<link href="https://fonts.googleapis.com/css2?family=Ubuntu:wght@400;500;700&family=Poppins:wght@400;500;600&display=swap" rel="stylesheet">
<style>
:root{
  --navy:#22335f;
  --navy-deep:#1d2c54;
  --orange:#f0612a;
  --ink:#222;
  --body:#555;
  --light:#f3f3f3;
  --white:#fff;
}
*{margin:0;padding:0;box-sizing:border-box}
html,body{width:1200px;height:3442px;overflow:hidden}
body{position:relative;background:var(--white);font-family:"Poppins",sans-serif;color:var(--body)}
.abs{position:absolute}
/* header */
.site-header{left:0;top:0;width:1200px;height:103px;background:var(--white)}
.brand{left:110px;top:22px;width:150px;text-align:center;font-family:"Poppins",sans-serif;font-weight:600;color:var(--navy);font-size:17px;line-height:22px}
.brand-dot{display:inline-block;width:14px;height:14px;border-radius:50%;background:var(--orange);margin-bottom:4px}
.topbar{right:120px;top:10px;display:flex;gap:34px;font-size:14px;color:var(--white)}
.topbar-strip{right:0;top:0;width:580px;height:42px;background:var(--orange);clip-path:polygon(6% 0,100% 0,100% 100%,0 100%)}
.topbar span{display:flex;align-items:center;gap:8px}
.main-nav{right:120px;top:60px;display:flex;gap:58px;font-size:14px;color:var(--ink)}
/* hero */
.hero{left:0;top:103px;width:1200px;height:466px;background:linear-gradient(180deg,#3a3430 0%,#5b4a3c 45%,#2e2a28 100%)}
.hero h1{left:0;top:252px;width:1200px;text-align:center;font-family:"Ubuntu",sans-serif;font-weight:700;font-size:46px;color:var(--white)}
.hero p{left:270px;top:326px;width:660px;text-align:center;font-size:15px;line-height:24px;color:var(--white)}
.btn{display:flex;align-items:center;gap:14px;background:var(--orange);color:var(--white);border-radius:30px;font-size:15px;font-weight:600;padding-left:6px;box-shadow:0 4px 10px rgba(0,0,0,.2)}
.btn-ring{width:40px;height:40px;border-radius:50%;border:4px solid var(--white);border-right-color:transparent}
.hero .btn{left:514px;top:406px;width:183px;height:55px}
/* customer types */
.segment{top:569px;height:342px}
.segment-business{left:0;width:600px;background:var(--navy)}
.segment-home{left:600px;width:600px;background:var(--orange)}
.segment h2{position:absolute;top:24px;left:0;width:100%;text-align:center;font-family:"Ubuntu",sans-serif;font-weight:400;font-size:38px;color:var(--white)}
.segment .rule{position:absolute;top:82px;left:50%;width:44px;height:2px;margin-left:-22px;background:var(--white)}
.segment .thumb{position:absolute;left:115px;top:112px;width:168px;height:168px;border-radius:50%;border:5px solid var(--white);background:linear-gradient(135deg,#c9ccd1,#8d939b)}
.segment p{position:absolute;left:303px;top:114px;width:250px;font-size:12.5px;line-height:24px;color:var(--white)}
.segment-home .thumb{left:56px}
.segment-home p{left:244px}
.segment-join{left:584px;top:724px;width:32px;height:32px;border-radius:50%;background:var(--white)}
/* section heads */
.section-title{left:0;width:1200px;text-align:center;font-family:"Ubuntu",sans-serif;font-weight:700;font-size:46px;color:var(--ink)}
.divider{left:560px;width:80px;height:8px}
.section-lead{left:180px;width:840px;text-align:center;font-size:12.5px;line-height:22px;color:var(--body)}
/* welcome */
.welcome-copy{left:112px;width:540px;font-size:12px;line-height:23px;color:var(--body)}
.welcome .btn{left:112px;top:1457px;width:163px;height:50px;font-size:14px}
.welcome .btn-ring{width:34px;height:34px}
.emblem{left:695px;top:1142px;width:400px;height:400px}
/* projects */
.project{top:1794px;height:298px;box-shadow:0 6px 14px rgba(0,0,0,.18)}
.p1{left:0;width:300px;background:linear-gradient(135deg,#eceff2,#9aa2ab)}
.p2{left:337px;width:301px;background:linear-gradient(180deg,#d7952c,#8a5a1d)}
.p3{left:677px;width:300px;background:linear-gradient(180deg,#d6a672,#5d4936)}
.p4{left:1012px;width:188px;background:linear-gradient(135deg,#dfe3e4,#6f7d6e)}
.quote-btn{left:516px;top:2186px;width:170px;height:53px;font-size:14px}
.quote-btn .btn-ring{width:34px;height:34px}
/* testimonials */
.card{top:2491px;width:307px;height:358px;background:var(--white);box-shadow:0 3px 14px rgba(0,0,0,.14)}
.card .badge{position:absolute;left:0;top:0;width:34px;height:34px;background:var(--orange);color:var(--white);font-family:"Ubuntu",sans-serif;font-weight:700;font-size:34px;line-height:44px;text-align:center}
.card .avatar{position:absolute;left:112px;top:33px;width:82px;height:82px;border-radius:50%;background:linear-gradient(180deg,#cfc6c2,#7a6a66)}
.card p{position:absolute;left:20px;top:132px;width:267px;text-align:center;font-size:13px;line-height:23.5px;color:var(--ink)}
.card .line{position:absolute;left:26px;top:285px;width:255px;height:1px;background:#e2e2e2}
.card .name{position:absolute;left:0;top:298px;width:100%;text-align:center;font-size:13px;color:var(--orange)}
.card .role{position:absolute;left:0;top:322px;width:100%;text-align:center;font-size:11px;color:var(--ink)}
/* footer */
.footer-shape{left:0;top:2960px;width:1200px;height:431px}
.footer-col{top:3110px;color:var(--white)}
.footer-col h3{font-family:"Ubuntu",sans-serif;font-weight:500;font-size:17px;margin-bottom:12px}
.footer-col ul{list-style:none;font-size:11.5px;line-height:31px}
.tweet{display:flex;gap:12px;margin-bottom:14px;font-size:11.5px;line-height:20px;font-weight:500}
.tweet-icon{flex:none;width:26px;height:26px;border-radius:50%;background:#3b8fd6;margin-top:6px}
.tweet em{color:var(--orange);font-style:normal}
.tweet small{display:block;font-size:9px;font-style:italic;line-height:14px;font-weight:400}
.footer-brand{left:955px;top:3180px;width:150px;text-align:center;color:var(--white);font-weight:600;font-size:16px;line-height:21px}
.footer-brand .brand-dot{background:var(--white)}
.legal{left:0;top:3391px;width:1200px;height:51px;background:var(--orange);color:var(--white);font-size:12px;text-align:center;line-height:51px}
</style>
</head>
<body>

<header>
  <div class="abs site-header"></div>
  <div class="abs topbar-strip"></div>
  <div class="abs brand"><span class="brand-dot"></span><br>Voltline Electrical</div>
  <div class="abs topbar">
    <span><svg width="16" height="16" viewBox="0 0 24 24"><path fill="#fff" d="M6.6 10.8a15 15 0 0 0 6.6 6.6l2.2-2.2c.3-.3.7-.4 1-.2 1.1.4 2.3.6 3.6.6.6 0 1 .4 1 1V20c0 .6-.4 1-1 1A17 17 0 0 1 3 4c0-.6.4-1 1-1h3.5c.6 0 1 .4 1 1 0 1.3.2 2.5.6 3.6.1.3 0 .7-.2 1z"/></svg><b style="font-size:18px;font-weight:500">+1 555 0142</b></span>
    <span><svg width="18" height="14" viewBox="0 0 24 18"><rect x="1" y="1" width="22" height="16" rx="2" fill="none" stroke="#fff" stroke-width="2"/><path d="M1 2l11 8 11-8" fill="none" stroke="#fff" stroke-width="2"/></svg>hello@voltline.example</span>
  </div>
  <nav class="abs main-nav"><span>Home</span><span>Meet the Team</span><span>Our Services</span><span>Projects</span><span>Contact Us</span></nav>
</header>

<section class="hero-wrap">
  <div class="abs hero" role="img" aria-label="Photo of a warm-lit modern home interior with an open staircase and pendant lighting"></div>
  <h1 class="abs hero-title" style="left:0;top:252px;width:1200px;text-align:center;font-family:'Ubuntu',sans-serif;font-weight:700;font-size:46px;color:#fff">We are Committed to WOWing You !</h1>
  <p class="abs" style="left:270px;top:326px;width:660px;text-align:center;font-size:15px;line-height:24px;color:#fff">Lorem ipsum dolor sit amet, consectetuer adipiscing elit, sed diam nonummy nibh euismod tincidunt ut laoreet dolore magna.</p>
  <div class="abs btn" style="left:514px;top:406px;width:183px;height:55px"><span class="btn-ring"></span>Get Started</div>
</section>

<section>
  <div class="abs segment segment-business">
    <h2>Business</h2><span class="rule"></span>
    <div class="thumb" role="img" aria-label="Photo of an open-plan office with ceiling lighting"></div>
    <p>Lorem ipsum dolor sit a consectetuer adipiscing elit, sed diam nonum nibh euismod tincidunt ut laoreore magna aliquam erat volutpat. Ut wisi enim ad minim veniam, quis nostr exerci tation ullamcorper suscipit lobortis ut aliquip ex ea commodo consequat.</p>
  </div>
  <div class="abs segment segment-home">
    <h2>House Owner</h2><span class="rule"></span>
    <div class="thumb" role="img" aria-label="Photo of a lit home interior"></div>
    <p>Lorem ipsum dolor sit a consectetuer adipiscing elit, sed diam nonum nibh euismod tincidunt ut laoreore magna aliquam erat volutpat. Ut wisi enim ad minim veniam, quis nostr exerci tation ullamcorper suscipit lobortis ut aliquip ex ea commodo consequat.</p>
  </div>
  <div class="abs segment-join"></div>
</section>

<section class="welcome">
  <h2 class="abs section-title" style="top:968px">Welcome</h2>
  <svg class="abs divider" style="top:1034px" viewBox="0 0 80 8"><line x1="0" y1="4" x2="32" y2="4" stroke="#bbb"/><line x1="48" y1="4" x2="80" y2="4" stroke="#bbb"/><circle cx="40" cy="4" r="3" fill="#f0612a"/></svg>
  <p class="abs section-lead" style="top:1057px">Lorem ipsum dolor sit amet, consectetuer adipiscing elit, sed diam nonummy nib euismod tincidunt ut laoreet dolore magna aliquam erat volutpat. Ut wisi enim ad min veniam, quis nostrud exerci tation ullamcorper suscipit lobortis</p>
  <p class="abs welcome-copy" style="top:1172px">Lorem ipsum dolor sit amet, consectetuer adipiscing elit, sed diam nonummy nib euismod tincidunt ut laoreet dolore magna aliquam erat volutpat. Ut wisi enim ad min veniam, quis nostrud exerci tation ullamcorper suscipit lobortis nisl ut aliquip ex mmodo consequat. Duis autem vel eum iriure dolor in hendrerit in vulputate velit esse molestie consequat, vel illum dolore eu feugiat</p>
  <p class="abs welcome-copy" style="top:1300px">Lorem ipsum dolor sit amet, consectetuer adipiscing elit, sed diam nonummy nib euismod tincidunt ut laoreet dolore magna aliquam erat volutpat. Ut wisi enim ad min veniam, quis nostrud exerci tation ullamcorper suscipit lobortis nisl ut aliquip ex mmodo consequat. Duis autem vel eum iriure dolor in hendrerit in vulputate velit esse molestie consequat, vel illum dolore eu feugiat</p>
  <div class="abs btn" style="left:112px;top:1457px;width:163px;height:50px;font-size:14px"><span class="btn-ring" style="width:34px;height:34px"></span>Know More</div>
  <svg class="abs emblem" viewBox="0 0 400 400">
    <path d="M30 170 A172 172 0 0 1 370 170" fill="none" stroke="#f0612a" stroke-width="26"/>
    <path d="M30 230 A172 172 0 0 0 370 230" fill="none" stroke="#f0612a" stroke-width="26"/>
    <circle cx="200" cy="200" r="150" fill="#fff" style="filter:drop-shadow(0 3px 8px rgba(0,0,0,.15))"/>
    <circle cx="200" cy="200" r="150" fill="#fff"/>
    <circle cx="200" cy="178" r="9" fill="#f0612a"/>
    <text x="200" y="222" text-anchor="middle" font-family="Poppins, sans-serif" font-weight="600" font-size="27" fill="#22335f">Voltline Electrical</text>
  </svg>
</section>

<section class="projects">
  <h2 class="abs section-title" style="top:1622px">Our Previous Projects</h2>
  <svg class="abs divider" style="top:1688px" viewBox="0 0 80 8"><line x1="0" y1="4" x2="32" y2="4" stroke="#bbb"/><line x1="48" y1="4" x2="80" y2="4" stroke="#bbb"/><circle cx="40" cy="4" r="3" fill="#f0612a"/></svg>
  <p class="abs section-lead" style="top:1710px">Lorem ipsum dolor sit amet, consectetuer adipiscing elit, sed diam nonummy nib euismod tincidunt ut laoreet dolore magna aliquam erat volutpat. Ut wisi enim ad min veniam, quis nostrud exerci tation ullamcorper suscipit lobortis</p>
  <div class="abs project p1" role="img" aria-label="Project photo: white office interior with recessed lighting"></div>
  <div class="abs project p2" role="img" aria-label="Project photo: corridor with warm golden wall lighting"></div>
  <div class="abs project p3" role="img" aria-label="Project photo: lounge with slatted ceiling and pendant lights"></div>
  <div class="abs project p4" role="img" aria-label="Project photo: bright open office with track lighting"></div>
  <div class="abs btn quote-btn"><span class="btn-ring"></span>Get A Quote</div>
</section>

<section class="testimonials">
  <h2 class="abs section-title" style="top:2303px">Our Testimonials</h2>
  <svg class="abs divider" style="top:2368px" viewBox="0 0 80 8"><line x1="0" y1="4" x2="32" y2="4" stroke="#bbb"/><line x1="48" y1="4" x2="80" y2="4" stroke="#bbb"/><circle cx="40" cy="4" r="3" fill="#f0612a"/></svg>
  <p class="abs section-lead" style="top:2388px">Lorem ipsum dolor sit amet, consectetuer adipiscing elit, sed diam nonummy nib euismod tincidunt ut laoreet dolore magna aliquam erat volutpat. Ut wisi enim ad min veniam, quis nostrud exerci tation ullamcorper suscipit lobortis</p>
  <article class="abs card" style="left:115px">
    <span class="badge">&ldquo;</span><div class="avatar" role="img" aria-label="Customer portrait"></div>
    <p>Lorem ipsum dolor sit a con adipiscing elit, sed diam nonum niblsmo tincidunt ut laoreore magna aliam erat volutpat. Ut wisi enim ad mini veniam, quis nostr exerci tation ullamcorper</p>
    <span class="line"></span><div class="name">Customer Name</div><div class="role">Dolor Nonum Niblsmo Tincidunt</div>
  </article>
  <article class="abs card" style="left:452px">
    <span class="badge">&ldquo;</span><div class="avatar" role="img" aria-label="Customer portrait"></div>
    <p>Lorem ipsum dolor sit a con adipiscing elit, sed diam nonum niblsmo tincidunt ut laoreore magna aliam erat volutpat. Ut wisi enim ad mini veniam, quis nostr exerci tation ullamcorper</p>
    <span class="line"></span><div class="name">Customer Name</div><div class="role">Dolor Nonum Niblsmo Tincidunt</div>
  </article>
  <article class="abs card" style="left:787px">
    <span class="badge">&ldquo;</span><div class="avatar" role="img" aria-label="Customer portrait"></div>
    <p>Lorem ipsum dolor sit a con adipiscing elit, sed diam nonum niblsmo tincidunt ut laoreore magna aliam erat volutpat. Ut wisi enim ad mini veniam, quis nostr exerci tation ullamcorper</p>
    <span class="line"></span><div class="name">Customer Name</div><div class="role">Dolor Nonum Niblsmo Tincidunt</div>
  </article>
</section>

<footer>
  <svg class="abs footer-shape" viewBox="0 0 1200 431" preserveAspectRatio="none"><polygon points="0,10 370,90 985,10 1200,114 1200,431 0,431" fill="#22335f"/></svg>
  <div class="abs footer-col" style="left:110px;width:340px">
    <h3>Latest Chirpnet</h3>
    <div class="tweet"><span class="tweet-icon"></span><div>Lorem ipsum dolor sit amet, conse adipiscing elit, sed diam <em>nonummy nib euismod</em><small>24th April, 2019</small></div></div>
    <div class="tweet"><span class="tweet-icon"></span><div>Lorem ipsum dolor sit amet, conse adipiscing elit, sed diam <em>nonummy nib euismod</em><small>24th April, 2019</small></div></div>
    <div class="tweet"><span class="tweet-icon"></span><div>Lorem ipsum dolor sit amet, conse adipiscing elit, sed diam <em>nonummy nib euismod</em><small>24th April, 2019</small></div></div>
  </div>
  <div class="abs footer-col" style="left:551px">
    <h3>Services</h3>
    <ul><li>Lorem Ipsum</li><li>Dolor sit amet,</li><li>Conse</li><li>Adipiscing</li><li>Lorem Ipsum</li><li>Dolor sit amet,</li></ul>
  </div>
  <div class="abs footer-col" style="left:771px">
    <h3>Company</h3>
    <ul><li>Home</li><li>Meet the Team</li><li>Our Services</li><li>Projects</li><li>Contact Us</li></ul>
  </div>
  <div class="abs footer-brand"><span class="brand-dot"></span><br>Voltline Electrical</div>
  <div class="abs legal">© All Rights Reserved, 2019</div>
</footer>

</body>
</html>
```